Thai Takeaway Menu Design

I need a menu re-design for a thai takeaway/restaurant in australia.

Please use content from the existing menu
http://www.platterwink.example/u/menu/7302918?p=1

I'd like to emphasise on
1 - free delivery for order over $40
2 - gluten free and vegetatian option available on most meal (however you want to word it - not fuss)

*remove (the banner order online and save $10)

I'm happy to change the whole concept & design. I particularly like rustic, raw look more than moden ones. Does not need to be flowery or anything like current one :)

Industry/Entity Type

Restaurant

```html
<!DOCTYPE html>
<html lang="en">
<head>
<meta charset="utf-8">
<title>Sawan Traditional Thai Cuisine – Takeaway Menu</title>
<link href="https://fonts.googleapis.com/css2?family=Cinzel:wght@400;700&family=Lora:wght@400;600&display=swap" rel="stylesheet">
<style>
:root{
  --backdrop:#8d7b6a;
  --choc:#3a1a10;
  --choc-mid:#5a2a16;
  --gold:#e0ab52;
  --gold-light:#f3cf86;
  --parch-dark:#6e3518;
  --parch-mid:#b06a2a;
  --parch-light:#e9b35e;
  --ink:#2a120a;
  --cream:#f5e3bf;
}
*{box-sizing:border-box;margin:0;padding:0}
html,body{width:849px;height:1200px;overflow:hidden}
body{background:var(--backdrop);font-family:'Lora',serif;color:var(--cream);position:relative}
.panel{position:absolute;left:14px;width:821px;box-shadow:0 4px 14px rgba(0,0,0,.45)}
.outer{top:14px;height:540px;background:linear-gradient(100deg,var(--parch-dark) 0%,var(--parch-mid) 45%,var(--parch-light) 80%,#d79a45 100%)}
.inner{top:580px;height:606px;background:radial-gradient(ellipse at 50% 40%,var(--choc-mid),var(--choc) 80%)}

/* outer: specials column */
.specials{position:absolute;left:0;top:0;width:200px;height:540px;background:var(--choc)}
.special{position:absolute;left:10px;width:180px;border:2px solid var(--gold);border-radius:10px;padding:16px 12px 10px 22px}
.special::before{content:"";position:absolute;inset:4px;border:1px solid var(--gold);border-radius:7px;opacity:.55}
.special h3{font-family:'Cinzel',serif;font-weight:700;font-size:15px;color:var(--gold-light);margin-bottom:6px}
.special li{list-style:none;font-size:10.5px;line-height:15px;color:var(--cream)}
.lunch{top:24px;height:166px}
.dinner{top:198px;height:134px}
.family{top:340px;height:184px}
.price-tag{position:absolute;left:-6px;top:-8px;width:34px;height:34px;border-radius:50%;background:var(--gold);color:var(--choc);font-family:'Cinzel',serif;font-weight:700;font-size:12px;display:flex;align-items:center;justify-content:center;border:2px solid var(--choc)}

/* outer: info column */
.info{position:absolute;left:270px;top:70px;width:250px;text-align:center;color:var(--cream)}
.info h2{font-family:'Cinzel',serif;font-size:19px;letter-spacing:1px;margin-bottom:8px}
.info .hours p{font-family:'Cinzel',serif;font-size:14px;line-height:20px}
.call{margin:28px auto 0;width:150px;padding:8px 0;background:var(--choc);border:1px solid var(--gold)}
.call span{display:block;font-family:'Cinzel',serif;font-weight:700;font-size:18px}
.call strong{display:block;font-family:'Cinzel',serif;font-size:20px;color:var(--cream)}
.address{margin-top:22px;font-size:10.5px;line-height:14px}

/* outer: brand column */
.brand{position:absolute;left:560px;top:40px;width:240px;text-align:center;color:var(--ink)}
.brand .name{font-family:'Cinzel',serif;font-weight:700;font-size:58px;letter-spacing:6px;margin-top:50px;line-height:1}
.brand .tagline{font-family:'Cinzel',serif;font-weight:700;font-size:14px;margin-top:6px;letter-spacing:.5px}
.services{position:absolute;right:50px;top:200px;text-align:center;font-family:'Cinzel',serif;font-size:16px;line-height:24px;color:var(--ink)}
.stamp{position:absolute;left:660px;top:392px}

/* inner menu */
.menu-col{position:absolute;top:22px;width:236px;display:flex;flex-direction:column;gap:9px}
.col-1{left:28px}.col-2{left:292px}.col-3{left:556px}
.section h4{position:relative;width:140px;margin:0 auto 6px;height:26px;border:1.5px solid var(--gold);border-radius:13px;font-family:'Cinzel',serif;font-size:13px;color:var(--gold-light);display:flex;align-items:center;justify-content:center}
.section h4::before,.section h4::after{content:"";position:absolute;top:12px;width:40px;height:1px;background:var(--gold)}
.section h4::before{right:100%}.section h4::after{left:100%}
.item{display:flex;justify-content:space-between;font-size:11px;line-height:15.5px;color:var(--cream);padding:0 4px}
.item b{font-weight:400;color:var(--gold-light)}
.dietary-note{margin-top:8px;padding:8px 10px;border:1px solid var(--gold);border-radius:8px;text-align:center;font-family:'Cinzel',serif;font-size:11px;line-height:16px;color:var(--gold-light)}
</style>
</head>
<body>

<section class="panel outer">
  <aside class="specials">
    <div class="special lunch"><span class="price-tag">$10</span>
      <h3>Lunch Special</h3>
      <ul><li>Spring Rolls</li><li>Soup of the Day</li><li>Any Curry with Rice</li><li>Thai Iced Tea</li><li>Available Wed to Sun</li></ul>
    </div>
    <div class="special dinner"><span class="price-tag">$35</span>
      <h3>Dinner for Two</h3>
      <ul><li>Spring Rolls</li><li>Satay Chicken</li><li>Two Main Dishes</li><li>Steamed Rice</li></ul>
    </div>
    <div class="special family"><span class="price-tag">$45</span>
      <h3>Family Pack</h3>
      <ul><li>Spring Rolls</li><li>Curry Puffs</li><li>Three Main Dishes</li><li>Pad Thai</li><li>Steamed Rice</li></ul>
    </div>
  </aside>

  <div class="info">
    <div class="hours">
      <h2>TRADING HOURS</h2>
      <p>Lunch</p>
      <p>(Wednesday - Sunday)</p>
      <p>11:00am - 2:30pm</p>
      <p>Dinner</p>
      <p>(Monday - Sunday)</p>
      <p>5:00pm - 9:30pm</p>
    </div>
    <div class="call"><span>CALL</span><strong>07 3900 4417</strong></div>
    <p class="address">212 Harlow Road, New Farm<br>Corner of Ashby St and Harlow Rd</p>
  </div>

  <div class="brand">
    <p class="name">SAWAN</p>
    <p class="tagline">Traditional Thai Cuisine</p>
  </div>
  <div class="services"><p>DINE IN</p><p>TAKEAWAY</p><p>DELIVERY</p></div>

  <svg class="stamp" width="124" height="124" viewBox="0 0 124 124">
    <circle cx="62" cy="62" r="58" fill="none" stroke="#3a1a10" stroke-width="3" opacity=".75"/>
    <circle cx="62" cy="62" r="50" fill="none" stroke="#3a1a10" stroke-width="1.2" opacity=".75"/>
    <rect x="10" y="49" width="104" height="26" fill="#3a1a10" opacity=".85"/>
    <text x="62" y="66" text-anchor="middle" font-family="Cinzel, serif" font-weight="700" font-size="12" textLength="90" lengthAdjust="spacingAndGlyphs" fill="#f5e3bf">FREE DELIVERY</text>
    <text x="62" y="38" text-anchor="middle" font-family="Lora, serif" font-size="9" fill="#3a1a10">ORDERS OVER</text>
    <text x="62" y="94" text-anchor="middle" font-family="Cinzel, serif" font-weight="700" font-size="13" fill="#3a1a10">$40</text>
  </svg>
</section>

<section class="panel inner">
  <div class="menu-col col-1">
    <div class="section"><h4>Entrée</h4>
      <p class="item">Spring Rolls<b>$7.50</b></p><p class="item">Curry Puffs<b>$8.00</b></p><p class="item">Satay Chicken<b>$9.00</b></p><p class="item">Fish Cakes<b>$9.50</b></p><p class="item">Prawn Crackers<b>$5.00</b></p><p class="item">Money Bags<b>$8.50</b></p><p class="item">Mixed Entree<b>$12.00</b></p>
    </div>
    <div class="section"><h4>Soup</h4>
      <p class="item">Tom Yum<b>$9.50</b></p><p class="item">Tom Kha<b>$9.50</b></p><p class="item">Wonton Soup<b>$8.50</b></p>
    </div>
    <div class="section"><h4>Curries</h4>
      <p class="item">Green Curry<b>$15.90</b></p><p class="item">Red Curry<b>$15.90</b></p><p class="item">Massaman Beef<b>$16.90</b></p><p class="item">Panang Curry<b>$15.90</b></p><p class="item">Jungle Curry<b>$15.90</b></p><p class="item">Yellow Curry<b>$15.90</b></p>
    </div>
    <div class="section"><h4>Vegetarian</h4>
      <p class="item">Mixed Vegetables<b>$13.90</b></p><p class="item">Tofu Cashew<b>$14.50</b></p><p class="item">Veg Green Curry<b>$14.50</b></p>
    </div>
    <div class="section"><h4>Beef</h4>
      <p class="item">Beef Oyster Sauce<b>$16.50</b></p><p class="item">Chilli Basil Beef<b>$16.50</b></p>
    </div>
  </div>

  <div class="menu-col col-2">
    <div class="section"><h4>Chicken</h4>
      <p class="item">Cashew Chicken<b>$15.90</b></p><p class="item">Garlic Chicken<b>$15.50</b></p><p class="item">Chilli Chicken<b>$15.50</b></p><p class="item">Sweet Sour Chicken<b>$15.50</b></p><p class="item">Ginger Chicken<b>$15.50</b></p><p class="item">Chicken Satay Stir Fry<b>$15.90</b></p>
    </div>
    <div class="section"><h4>Pork</h4>
      <p class="item">Sweet Sour Pork<b>$15.50</b></p><p class="item">Garlic Pork<b>$15.50</b></p><p class="item">Crispy Pork Chilli<b>$16.50</b></p>
    </div>
    <div class="section"><h4>Duck</h4>
      <p class="item">Red Duck Curry<b>$19.90</b></p><p class="item">Crispy Duck Tamarind<b>$19.90</b></p><p class="item">Roast Duck Stir Fry<b>$19.50</b></p>
    </div>
    <div class="section"><h4>Seafood</h4>
      <p class="item">Garlic Prawns<b>$18.90</b></p><p class="item">Chilli Squid<b>$17.90</b></p><p class="item">Fish Chilli Sauce<b>$18.50</b></p><p class="item">Prawn Red Curry<b>$18.90</b></p><p class="item">Salt Pepper Squid<b>$17.90</b></p><p class="item">Seafood Combo<b>$19.90</b></p><p class="item">Basil Mussels<b>$18.50</b></p>
    </div>
  </div>

  <div class="menu-col col-3">
    <div class="section"><h4>Noodles</h4>
      <p class="item">Pad Thai<b>$14.90</b></p><p class="item">Pad See Ew<b>$14.90</b></p><p class="item">Drunken Noodles<b>$14.90</b></p><p class="item">Rad Na<b>$14.90</b></p><p class="item">Singapore Noodles<b>$14.90</b></p>
    </div>
    <div class="section"><h4>Rice</h4>
      <p class="item">Steamed Rice<b>$3.00</b></p><p class="item">Coconut Rice<b>$4.00</b></p><p class="item">Fried Rice<b>$12.90</b></p><p class="item">Pineapple Rice<b>$14.50</b></p><p class="item">Sticky Rice<b>$4.00</b></p>
    </div>
    <div class="section"><h4>Dessert</h4>
      <p class="item">Black Sticky Rice<b>$7.50</b></p><p class="item">Banana Fritters<b>$7.50</b></p><p class="item">Coconut Ice Cream<b>$6.50</b></p>
    </div>
    <div class="section"><h4>Drinks</h4>
      <p class="item">Thai Iced Tea<b>$4.50</b></p><p class="item">Soft Drinks<b>$3.00</b></p><p class="item">Mineral Water<b>$3.00</b></p><p class="item">Coconut Juice<b>$4.50</b></p><p class="item">Iced Coffee<b>$4.50</b></p>
    </div>
    <p class="dietary-note">Gluten free &amp; vegetarian options<br>available on most dishes – just ask</p>
  </div>
</section>

</body>
</html>
```